Rework of Honey Labels - Updated for clarity

I am looking for a re-do of our current creamed honey labels.
Creamed honey is a butter-consistency. There are 5 flavors - original, lavender, chocolate, lemon, cinnamon. We want for it to look sophisticated and luxurious. We want the labels to all be cohesive in this group, but to be able to easily tell the difference between the products by color or something quick besides just words to tell the difference in the product. The product will be an off-white/light amber - except for the chocolate which is the color of Cremoso. There are three size containers for each of these honeys. But we can just focus on the single size for this contest.
The honey market in our area is extremely competitive. Right now, I feel our labels look more homemade. I want something that stands out. We charge a premium for our products. We want for our labels to look like we are a superior product. We are getting our product in many local stores and need to differentiate ourselves. I am attaching some of the labels that I think stand out. As for the labels themselves. They can include that whole blurb about us as Brookvale Meadow - or not. It is not truly necessary to have on the labels. But the logo needs to be included.
For all of these, we want something unique and special. Like you are going for an English mid-day tea at an upscale hotel in London with the Queen (well, I guess now the King...but really I think of the Queen).
I am uploading our current labels and then a few labels to take inspiration from.
Updates
I just reworked the description to be more limited in what I was asking for. Looking for a label for creamed honey in one size jar only. Thank you.

```html
<!DOCTYPE html>
<html lang="en">
<head>
<meta charset="utf-8">
<title>Brookvale Meadow – Lavender Infused Honey Label</title>
<link rel="stylesheet" href="https://fonts.googleapis.com/css2?family=Cinzel:wght@400;500&family=Josefin+Sans:wght@300;400;700&family=Arimo:wght@400;700&display=swap">
<style>
  :root{
    --bg:#ededed;
    --maroon:#340204;
    --gold:#857226;
    --gold-text:#b09a4c;
    --lavender:#c9c9e0;
    --cream:#e6e6f2;
    --ink:#3a0a0c;
  }
  html,body{margin:0;padding:0;width:1200px;height:1058px;overflow:hidden;background:var(--bg);}
  .label-sheet{display:block;width:1200px;height:1058px;}
  .fill-maroon{fill:var(--maroon);}
  .fill-gold{fill:var(--gold);}
  .fill-lavender{fill:var(--lavender);}
  .line-gold{fill:none;stroke:var(--gold);stroke-width:3;}
  .line-cream{fill:none;stroke:var(--cream);stroke-width:3;}
  .brand-name{font-family:"Cinzel",serif;font-weight:500;fill:var(--cream);}
  .pure{font-family:"Cinzel",serif;font-size:36px;fill:var(--cream);}
  .infused{font-family:"Josefin Sans",sans-serif;font-weight:700;font-size:70px;letter-spacing:10px;fill:var(--cream);}
  .honey{font-family:"Josefin Sans",sans-serif;font-weight:300;fill:var(--cream);}
  .flavor{font-family:"Cinzel",serif;font-size:36px;fill:var(--ink);}
  .grade{font-family:"Cinzel",serif;font-size:20px;fill:var(--ink);}
  .blurb{font-family:"Josefin Sans",sans-serif;font-weight:300;font-size:29px;fill:var(--gold-text);}
  .tag-text{font-family:"Cinzel",serif;font-size:28px;fill:var(--ink);}
  .nutri-title{font-family:"Arimo",sans-serif;font-weight:700;font-size:25px;fill:var(--gold-text);}
  .nutri{font-family:"Arimo",sans-serif;font-size:16px;fill:var(--gold-text);}
  .footer-note{font-family:"Arimo",sans-serif;font-size:14px;fill:var(--gold-text);}
  .icon{fill:none;stroke:var(--gold-text);stroke-width:2;}
</style>
</head>
<body>
<svg class="label-sheet" viewBox="30 532 1970 1737" xmlns="http://www.w3.org/2000/svg">

  <!-- Neck tag -->
  <g class="neck-tag">
    <polygon class="fill-gold" points="148,1040 362,1040 468,1225 362,1410 148,1410 37,1225"/>
    <polygon class="fill-maroon" points="154,1050 356,1050 456,1225 356,1400 154,1400 49,1225"/>
    <polygon class="line-gold" points="162,1063 348,1063 441,1225 348,1387 162,1387 69,1225"/>
    <polygon class="fill-lavender" points="166,1070 344,1070 433,1225 344,1380 166,1380 77,1225"/>
    <polygon class="fill-maroon" points="173,1083 337,1083 418,1225 337,1367 173,1367 92,1225"/>

    <circle class="fill-lavender" cx="255" cy="1180" r="48"/>
    <text class="brand-name" x="255" y="1275" font-size="28" text-anchor="middle">MEADOWLARK</text>
    <text class="brand-name" x="255" y="1310" font-size="28" text-anchor="middle">APIARY</text>

    <polygon class="fill-gold" points="162,1404 348,1404 348,1738 255,1772 162,1738"/>
    <polygon class="fill-maroon" points="168,1410 342,1410 342,1732 255,1763 168,1732"/>
    <polygon class="fill-lavender" points="180,1412 330,1412 330,1712 255,1740 180,1712"/>
    <polygon class="line-cream" points="188,1412 322,1412 322,1706 255,1731 188,1706"/>
    <text class="tag-text" transform="translate(245 1565) rotate(-90)" text-anchor="middle" font-size="26">•PREMIUM QUALITY•</text>
    <line x1="257" y1="1470" x2="257" y2="1660" stroke="var(--ink)" stroke-width="2"/>
    <text class="tag-text" transform="translate(287 1565) rotate(-90)" text-anchor="middle">LAVENDER</text>
  </g>

  <!-- Wrap label -->
  <g class="wrap-label">
    <rect class="fill-gold" x="505" y="1118" width="1485" height="519"/>
    <rect class="fill-maroon" x="505" y="1137" width="1485" height="480"/>

    <!-- Front hexagon -->
    <polygon class="fill-gold" points="1062,1068 1432,1068 1625,1378 1432,1688 1062,1688 868,1378"/>
    <polygon class="fill-maroon" points="1070,1080 1425,1080 1612,1378 1425,1676 1070,1676 881,1378"/>
    <polygon class="line-gold" points="1086,1096 1409,1096 1590,1378 1409,1660 1086,1660 905,1378"/>
    <polygon class="fill-lavender" points="1095,1105 1400,1105 1572,1378 1400,1651 1095,1651 922,1378"/>
    <polygon class="fill-maroon" points="1106,1122 1389,1122 1548,1378 1389,1634 1106,1634 946,1378"/>

    <text class="brand-name" x="1247" y="1284" font-size="30" text-anchor="middle">BROOKVALE MEADOW</text>
    <line x1="1150" y1="1304" x2="1345" y2="1304" stroke="var(--cream)" stroke-width="1.5"/>

    <text class="pure" x="1247" y="1356" text-anchor="middle">100% PURE</text>
    <text class="infused" x="1252" y="1430" text-anchor="middle">INFUSED</text>
    <text class="honey" x="1247" y="1515" text-anchor="middle"><tspan font-size="96">H</tspan><tspan font-size="82">ONEY</tspan></text>

    <rect role="img" aria-label="Lavender sprig ornament" class="fill-lavender" x="1000" y="1394" width="46" height="60" rx="18" opacity="0.35"/>
    <rect role="img" aria-label="Lavender sprig ornament" class="fill-lavender" x="1442" y="1394" width="46" height="60" rx="18" opacity="0.35"/>

    <rect class="fill-lavender" x="1043" y="1535" width="409" height="48"/>
    <text class="flavor" x="1247" y="1572" text-anchor="middle">LAVENDER</text>
    <rect class="fill-lavender" x="1068" y="1588" width="358" height="52"/>
    <text class="grade" x="1247" y="1609" text-anchor="middle">US GRADE A FANCY</text>
    <text class="grade" x="1247" y="1632" text-anchor="middle">NET WT.: 16 OZ / 453.6 G</text>

    <!-- Side blurb -->
    <g class="blurb" text-anchor="middle">
      <text x="659" y="1210">This raw honey is</text>
      <text x="659" y="1246">whipped for a smooth</text>
      <text x="659" y="1282">and spreadable</text>
      <text x="659" y="1318">texture. Try it on toast,</text>
      <text x="659" y="1354">pancakes, peanut</text>
      <text x="659" y="1390">butter and honey</text>
      <text x="659" y="1426">sandwiches. Soon to</text>
      <text x="659" y="1462">be your favorite!</text>
      <text x="659" y="1532">100% Pure Honey</text>
      <text x="659" y="1568">No Additives</text>
    </g>

    <!-- Nutrition panel -->
    <g class="nutrition">
      <rect x="1690" y="1145" width="282" height="274" fill="none" stroke="var(--gold)" stroke-width="2"/>
      <text class="nutri-title" x="1699" y="1174">Nutrition Information</text>
      <line x1="1690" y1="1182" x2="1972" y2="1182" stroke="var(--gold)" stroke-width="2"/>
      <g class="nutri">
        <text x="1698" y="1198">Servings per package:</text><text x="1963" y="1198" text-anchor="end">25.00</text>
        <text x="1698" y="1217">Serving size:</text><text x="1963" y="1217" text-anchor="end">10.00 g</text>
      </g>
      <line x1="1690" y1="1223" x2="1972" y2="1223" stroke="var(--gold)" stroke-width="2"/>
      <g class="nutri" text-anchor="end">
        <text x="1866" y="1237">Average</text><text x="1963" y="1237">Average</text>
        <text x="1866" y="1256">Quantity per</text><text x="1963" y="1256">Quantity per</text>
        <text x="1866" y="1275">Serving</text><text x="1963" y="1275">100 g</text>
      </g>
      <line x1="1690" y1="1280" x2="1972" y2="1280" stroke="var(--gold)" stroke-width="2"/>
      <g class="nutri">
        <text x="1698" y="1296">Energy</text><text x="1866" y="1296" text-anchor="end">140 kJ</text><text x="1963" y="1296" text-anchor="end">1400 kJ</text>
        <text x="1698" y="1315">Protein</text><text x="1866" y="1315" text-anchor="end">0.0 g</text><text x="1963" y="1315" text-anchor="end">0.2 g</text>
        <text x="1698" y="1335">Fat, total</text><text x="1866" y="1335" text-anchor="end">0.0 g</text><text x="1963" y="1335" text-anchor="end">0.0 g</text>
        <text x="1698" y="1354">-saturated</text><text x="1866" y="1354" text-anchor="end">0.0 g</text><text x="1963" y="1354" text-anchor="end">0.0 g</text>
        <text x="1698" y="1374">Carbohydrate</text><text x="1866" y="1374" text-anchor="end">8.2 g</text><text x="1963" y="1374" text-anchor="end">82.1 g</text>
        <text x="1698" y="1393">-sugars</text><text x="1866" y="1393" text-anchor="end">8.2 g</text><text x="1963" y="1393" text-anchor="end">82.1 g</text>
        <text x="1698" y="1413">Sodium</text><text x="1866" y="1413" text-anchor="end">1 mg</text><text x="1963" y="1413" text-anchor="end">14 mg</text>
      </g>

      <!-- Storage & warning icons -->
      <g class="icon">
        <circle cx="1754" cy="1452" r="24"/>
        <rect x="1750" y="1436" width="8" height="22" rx="4"/>
        <circle cx="1754" cy="1462" r="6"/>
        <polygon points="1862,1430 1886,1474 1838,1474"/>
        <line x1="1862" y1="1445" x2="1862" y2="1461" stroke-width="3"/>
        <circle cx="1862" cy="1467" r="1.5" fill="var(--gold-text)"/>
        <circle cx="1916" cy="1452" r="24"/>
        <rect x="1908" y="1438" width="16" height="28" rx="5"/>
        <line x1="1899" y1="1469" x2="1933" y2="1435"/>
      </g>
      <g class="footer-note">
        <text x="1751" y="1495" text-anchor="middle">Store at room</text>
        <text x="1751" y="1514" text-anchor="middle">temperature</text>
        <text x="1810" y="1495"><tspan text-decoration="underline">Warning:</tspan> Honey is not</text>
        <text x="1810" y="1514">suitable for children</text>
        <text x="1810" y="1533">under 12 months</text>
      </g>
      <g class="footer-note" text-anchor="middle">
        <text x="1831" y="1552">Produced by: Meadowlark Apiary</text>
        <text x="1831" y="1571">Brookvale Meadow</text>
        <text x="1831" y="1591">N4150, Hollow Lane,</text>
        <text x="1831" y="1611">Pine Ridge, WI 54100</text>
      </g>
    </g>
  </g>
</svg>
</body>
</html>
```